Christmas social media advert post

I am looking for an eye catching advert for use mainly on social media posts.
The following is the detail of the event.

Christmas special offer-
£10pp,– offer includes –
Half an hour Toboggan track,
Half an hour Slingshot paintballs (20 paintballs pp) and safe target archery (under cover and indoor ranges). Activities all the family from age 4 to grandparents can join in,
Also available – Add on indoor activities including Mini Curling, Bead Blitz, Safe axe throwing, Air juggler – from £3.50pp and age 6plus
Café open for hot food and drinks in the ‘Fireside Frost Lodge and the heated Christmas marquee.

A basic idea I put together for what I feel is the important information is -

Christmas Special offer -
Starts Saturday 20th December.
£10pp – offer includes –
Half an hour Slingshot paintballs (20 paintballs pp) and safe target archery (under cover and indoor ranges). Activities all the family from age 4 to grandparents can join in. Booking is essential - details on how below.
Also available Add on indoor activities - including Mini Curling, Bead Blitz, Safe axe throwing, Air juggler – from £3.50pp and age 6plus.
Ages start from 4 plus.
All activities are great for children and adults so perfect for families as well as friends, parties and get togethers.
Free huge car parks,
Booking is easy-
Just Message from messenger (on this post) or email
martin@hollowbrookleisurepark.co.uk for availability of your preferred date and time.

I would be happy to send the detailed information to enquiries if it meant a better looking advert / post.

Full details are in the picture uploads, feel free to use as much or as little of the information as you feel best.

```html
<!DOCTYPE html>
<html lang="en">
<head>
<meta charset="utf-8">
<title>Christmas Special Offer</title>
<link href="https://fonts.googleapis.com/css2?family=Prata&family=Mulish:wght@300;400;600;800&display=swap" rel="stylesheet">
<style>
  :root {
    --cream: #efe9da;
    --red: #c21f35;
    --ink: #1c1a1a;
    --pine: #2f5a3a;
    --pine-dark: #1f3d28;
    --gold: #c9a45a;
    --ornament: #c9d3b8;
  }
  * { margin: 0; padding: 0; box-sizing: border-box; }
  html, body { width: 1200px; height: 1200px; overflow: hidden; background: var(--cream); }
  .advert {
    position: relative; width: 1200px; height: 1200px; overflow: hidden;
    background: var(--cream);
    font-family: "Mulish", sans-serif; color: var(--ink);
  }
  .garland-frame { position: absolute; inset: 0; }
  .flourish {
    position: absolute; left: 500px; width: 200px; height: 46px;
    background: radial-gradient(ellipse at center, var(--ornament) 0%, rgba(201,211,184,0.3) 60%, transparent 75%);
  }
  .flourish--top { top: 227px; }
  .flourish--bottom { top: 420px; }
  .headline {
    position: absolute; top: 262px; left: 0; width: 1200px; text-align: center;
    font-family: "Prata", serif; font-size: 112px; line-height: 1; color: var(--red);
  }
  .subhead {
    position: absolute; top: 366px; left: 0; width: 1200px; text-align: center;
    font-size: 46px; font-weight: 300; letter-spacing: 0.5px; line-height: 1;
  }
  .band {
    position: absolute; left: 271px; width: 658px; height: 44px;
    background: var(--red); color: #fff; text-align: center;
    font-weight: 800; font-size: 31px; line-height: 44px;
  }
  .band--price { top: 500px; }
  .band--extras { top: 737px; }
  .activity {
    position: absolute; left: 0; width: 1200px; text-align: center;
    font-size: 32px; font-weight: 300; line-height: 1;
  }
  .activity em { font-style: normal; font-weight: 600; color: var(--red); }
  .activity--toboggan { top: 553px; }
  .activity--slingshot { top: 610px; }
  .details {
    position: absolute; left: 0; width: 1200px; text-align: center;
    font-size: 20.5px; line-height: 27px; font-weight: 400;
  }
  .details--included { top: 642px; }
  .details--addons { top: 798px; }
  .details--cafe { top: 858px; }
  .details strong { font-weight: 800; }
  .details .venue { color: var(--red); font-weight: 600; }
  .gallery-photo {
    position: absolute; top: 936px; width: 168px; height: 168px; border-radius: 50%;
    border: 5px solid var(--cream);
    box-shadow: 0 4px 10px rgba(0,0,0,0.25);
  }
</style>
</head>
<body>
<main class="advert">
  <svg class="garland-frame" width="1200" height="1200" viewBox="0 0 1200 1200" role="img" aria-label="Christmas garland of pine branches with red and gold baubles framing the offer">
    <defs>
      <radialGradient id="pineTone" cx="50%" cy="50%" r="75%">
        <stop offset="55%" stop-color="#3d6b45"/>
        <stop offset="100%" stop-color="#1f3d28"/>
      </radialGradient>
    </defs>
    <path fill="url(#pineTone)" fill-rule="evenodd"
      d="M0 0H1200V1200H0Z
         M230 190 Q400 130 560 175 Q700 230 860 170 Q960 150 990 230
         Q960 400 1000 560 Q980 760 990 930 Q900 990 760 960
         Q600 1010 420 970 Q280 1000 230 930 Q200 760 215 560 Q170 380 230 190Z"/>
  </svg>

  <div class="flourish flourish--top" role="img" aria-label="Holly and reindeer flourish"></div>
  <h1 class="headline">Christmas</h1>
  <p class="subhead">SPECIAL OFFER-</p>
  <div class="flourish flourish--bottom" role="img" aria-label="Holly and reindeer flourish"></div>

  <div class="band band--price">£10pp,– OFFER INCLUDES</div>
  <p class="activity activity--toboggan">Half an hour <em>Toboggan track,</em></p>
  <p class="activity activity--slingshot">Half an hour <em>Slingshot paintballs</em></p>
  <p class="details details--included">(20 paintballs pp) and safe target archery (under cover and<br>indoor ranges). Activities all the family from age 4 to<br>grandparents can join in,</p>

  <div class="band band--extras">Also available</div>
  <p class="details details--addons">Add on indoor activities including Mini Curling, Bead Blitz,<br>Safe axe throwing, Air juggler from <strong>£3.50pp</strong> and age 6plus</p>
  <p class="details details--cafe">Café open for hot food and drinks in the<br><span class="venue">‘Fireside Frost Lodge</span> and the heated Christmas marquee</p>

  <div class="gallery-photo" style="left:229px;background:linear-gradient(135deg,#6b5a4a,#2e3b4a);" role="img" aria-label="Photo of a young player at the slingshot paintball range"></div>
  <div class="gallery-photo" style="left:363px;background:linear-gradient(135deg,#3a5a9a,#c8b49a);" role="img" aria-label="Photo of axe throwing target with safe axes"></div>
  <div class="gallery-photo" style="left:503px;background:linear-gradient(135deg,#a88a66,#5a4a3a);" role="img" aria-label="Photo of an archer at the indoor archery range"></div>
  <div class="gallery-photo" style="left:643px;background:linear-gradient(135deg,#9a7048,#d8b88a);" role="img" aria-label="Photo of hot chocolates in the cosy wooden cabin"></div>
  <div class="gallery-photo" style="left:789px;background:linear-gradient(135deg,#b89a70,#e0cfae);" role="img" aria-label="Photo of a player on the mini curling lane"></div>
</main>
</body>
</html>
```